SEO and image area for top of invitation website

We need to add an area on our final category pages for SEO text. Instead of just adding text, we'd like to develop a graphical approach that keeps with our soft, feminine look.

You can view an example of our current final category page at http://www.partywren.example/invitations/boy-birthday

I've attached an image of what we're thinking it could look like, but you're welcome to alter the design.

The area should be the same width as our site, but can be any height you determine appropriate.

The winner of this project may be approached to develop the additional designs and backgrounds for us as another project. We additionally have several other projects we're interested in doing with the winner.

We have had a question about the right side of the banner, and what "Free Unlimited Proofs" mean.

About Free Unlimited Proofs:

We are a custom invitation printing company. When a customer orders an invitation from us, they tell us what information we want on the invitation. We then create an electronic sample, or "proof", of what it will look like. We then email it to the customer and they can tell us if they want to make any more changes. We will continue to send them samples, or what we call "proofs", until they are completely satisfied with the way it looks.

We offer Free UNLIMITED Proofs. Compared to our competitors, we are the only one to offer free unlimited proofs.

So, for the right side of this banner, we need an image, or a badge, promoting that we offer free unlimited proofs, and you can include that we are the only ones to do it, if your design has space for that information.

Also, keep in mind, that for other category pages, we may create different images or badges to put in this area - such as for our Low Price Guarantee or to promote a coupon or specific product, for example. So, your design should be able to work with various images on the right side.

Target Market(s)

Our demographic is 100% women, ages 25-60.

Industry/Entity Type

Seo

Requirements
Must have
• The area must have 3 things:
1) Area for the title of the page.
2) Area for SEO text describing the category page.
3) Area for an image. Keep in mind that this image may change for each category page. For this project, you will create an image for our offering of "Free Unlimited Proofs". On other pages, we may display other images we create such as "Low Price Guarantee" or images of certain products we'd like to promote. Just keep this in mind when you're making the design flow.
Nice to have
• Optional: Light design background. We wouldn't mind there being a slight graphical background to this area, to keep it interesting to the eye. Then, for other category pages, we may make additional backgrounds to use in this box area.

```html
<!DOCTYPE html>
<html lang="en">
<head>
<meta charset="utf-8">
<title>Boy Birthday Invitations</title>
<link href="https://fonts.googleapis.com/css2?family=Pacifico&family=Oswald:wght@700&display=swap" rel="stylesheet">
<style>
  :root {
    --sky: #2aa3e3;
    --sky-light: #5cc4f4;
    --sky-deep: #1479c4;
    --title-yellow: #ffd21a;
    --title-shade: #f0a400;
    --board: #ffffff;
    --stick: #b98a5c;
    --accent-yellow: #f7c400;
    --panel-grey: #ececec;
    --ribbon: #1d8fdc;
    --ribbon-dark: #0d5fa8;
    --ribbon-light: #4cb6f2;
    --proof-yellow: #ffe21a;
    --card-yellow: #f3cf3a;
    --card-green: #7cc25a;
    --card-blue: #5ec0ec;
  }
  html, body {
    margin: 0;
    padding: 0;
    overflow: hidden;
    background: #ffffff;
  }
  .banner {
    position: relative;
    width: 1200px;
    height: 246px;
    overflow: hidden;
    background: radial-gradient(ellipse 70% 120% at 40% 65%, var(--sky-light) 0%, var(--sky) 70%);
  }
  .page-title {
    position: absolute;
    left: 34px;
    top: -6px;
    margin: 0;
    font-family: "Pacifico", cursive;
    font-weight: 400;
    font-size: 60px;
    line-height: 1.4;
    color: var(--title-yellow);
    white-space: nowrap;
    text-shadow:
      0 2px 0 var(--title-shade),
      3px 0 0 var(--sky-deep), -3px 0 0 var(--sky-deep),
      0 4px 0 var(--sky-deep), 0 -3px 0 var(--sky-deep),
      3px 4px 0 var(--sky-deep), -3px 4px 0 var(--sky-deep),
      3px -3px 0 var(--sky-deep), -3px -3px 0 var(--sky-deep),
      0 0 14px #8fd8fa;
  }
  .hanger {
    position: absolute;
    width: 40px;
    height: 6px;
    background: var(--stick);
    border-radius: 2px;
  }
  .hanger--left { left: 16px; top: 114px; transform: rotate(-34deg); }
  .hanger--right { left: 684px; top: 104px; transform: rotate(34deg); }
  .seo-board {
    position: absolute;
    left: 37px;
    top: 114px;
    width: 675px;
    height: 123px;
    background: var(--board);
    box-shadow: 0 2px 4px rgba(0, 60, 120, 0.25);
  }
  .promo-panel {
    position: absolute;
    left: 0;
    top: 0;
    width: 1200px;
    height: 246px;
  }
  .proof-samples {
    position: absolute;
    left: 892px;
    top: 12px;
    width: 218px;
    height: 122px;
    border-radius: 4px;
    background: linear-gradient(100deg, var(--card-yellow) 0%, var(--card-green) 55%, var(--card-blue) 100%);
    transform: rotate(-2deg);
  }
  .proof-ribbon {
    position: absolute;
    left: 840px;
    top: 118px;
    width: 358px;
    height: 100px;
  }
  .ribbon-text {
    position: absolute;
    left: 900px;
    top: 134px;
    width: 234px;
    text-align: center;
    font-family: "Oswald", sans-serif;
    font-weight: 700;
    line-height: 1;
    color: var(--proof-yellow);
  }
  .ribbon-text .headline {
    display: block;
    font-size: 42px;
    text-shadow: 0 2px 0 var(--ribbon-dark);
  }
  .ribbon-text .subline {
    display: block;
    margin-top: 2px;
    font-size: 30px;
    text-shadow: 0 2px 0 var(--ribbon-dark);
  }
</style>
</head>
<body>
  <section class="banner">
    <h1 class="page-title">Boy Birthday Invitations</h1>
    <span class="hanger hanger--left"></span>
    <span class="hanger hanger--right"></span>
    <div class="seo-board"></div>

    <svg class="promo-panel" viewBox="0 0 1200 246" aria-hidden="true">
      <path d="M850 0 Q800 123 854 246 L1200 246 L1200 0 Z" fill="var(--accent-yellow)"/>
      <path d="M870 0 Q820 123 874 246 L1200 246 L1200 0 Z" fill="var(--panel-grey)"/>
    </svg>

    <div class="proof-samples" role="img" aria-label="Fanned stack of sample boy birthday invitation cards"></div>

    <svg class="proof-ribbon" viewBox="0 0 358 100" aria-hidden="true">
      <defs>
        <linearGradient id="ribbonFace" x1="0" y1="0" x2="0" y2="1">
          <stop offset="0" stop-color="var(--ribbon-light)"/>
          <stop offset="1" stop-color="var(--ribbon)"/>
        </linearGradient>
      </defs>
      <polygon points="0,20 58,20 58,68 0,68 16,44" fill="var(--ribbon)"/>
      <polygon points="358,20 300,20 300,68 358,68 342,44" fill="var(--ribbon)"/>
      <polygon points="58,68 70,82 70,68" fill="var(--ribbon-dark)"/>
      <polygon points="300,68 288,82 288,68" fill="var(--ribbon-dark)"/>
      <rect x="57" y="4" width="244" height="90" fill="url(#ribbonFace)"/>
    </svg>

    <div class="ribbon-text">
      <span class="headline">UNLIMITED</span>
      <span class="subline">PROOFS</span>
    </div>
  </section>
</body>
</html>
```